Redesign of an insurance website

Attached is an insurance website that I need to redesign. Currently the website is too dark. I like for example www.brenvalo.com . Could you make the website lighter and change the structure a little so that it is more user friendly?

Industry/Entity Type

Insurance

Number of Pages Required

4 page

```html
<!DOCTYPE html>
<html lang="en">
<head>
<meta charset="utf-8">
<title>Kryjto.cz – Insurance &amp; Financial Planning</title>
<link href="https://fonts.googleapis.com/css2?family=Montserrat:wght@400;500;600;700;800&family=Poppins:wght@300;400;500;600&display=swap" rel="stylesheet">
<style>
:root{
  --navy:#1d3866;
  --navy-dark:#15294d;
  --teal:#117a68;
  --teal-dark:#0c5f52;
  --yellow:#f6d523;
  --grey-bg:#f4f5f7;
  --nav-bg:#d9dbde;
  --text:#6b7078;
  --heading:#1f2a3a;
  --white:#ffffff;
}
*{margin:0;padding:0;box-sizing:border-box}
html,body{width:1200px;height:4235px;overflow:hidden}
body{font-family:'Poppins',sans-serif;color:var(--text);background:var(--white);position:relative;font-size:13px;line-height:1.65}
h1,h2,h3,h4{font-family:'Montserrat',sans-serif;color:var(--heading)}
section,header,footer,.topbar,.main-nav{position:absolute;left:0;width:1200px}
.abs{position:absolute}

/* top bar */
.topbar{top:0;height:40px;background:var(--navy-dark);color:#cfd6e4;font-size:12px}
.topbar .welcome{left:51px;top:11px}
.topbar .social{left:505px;top:13px;display:flex;gap:30px}
.topbar .social span{width:13px;height:13px;border-radius:50%;background:#cfd6e4;display:block}
.topbar .search{left:1030px;top:9px;width:150px;height:22px;background:#26406d;border-radius:2px}

/* header */
.site-header{top:40px;height:118px;background:var(--white)}
.logo{left:51px;top:46px;font-family:'Montserrat',sans-serif;font-weight:800;font-size:27px;color:var(--navy);letter-spacing:.5px}
.header-band{left:330px;top:0;width:870px;height:118px;background:var(--teal);clip-path:polygon(30px 0,100% 0,100% 100%,80px 100%)}
.header-stripe{left:322px;top:0;width:70px;height:118px;background:var(--yellow);clip-path:polygon(0 0,30px 0,80px 100%,50px 100%)}
.contact-chip{top:43px;display:flex;gap:12px;align-items:center;color:#e2f1ed;font-size:12px;line-height:1.35}
.contact-chip strong{color:var(--white);font-weight:500;font-size:14px;display:block}
.quote-btn{left:1000px;top:48px;width:152px;height:36px;background:var(--yellow);color:var(--heading);font-family:'Montserrat',sans-serif;font-weight:700;font-size:13px;display:flex;align-items:center;justify-content:center}

/* hero */
.hero{top:158px;height:477px;background:linear-gradient(120deg,#2a3848 0%,#55667a 40%,#7f8fa0 65%,#3d4c5e 100%)}
.hero::after{content:"";position:absolute;inset:0;background:rgba(20,30,45,.35)}
.hero-photo{position:absolute;inset:0}
.main-nav{top:158px;height:57px;background:rgba(217,219,222,.92);z-index:3}
.main-nav ul{list-style:none}
.main-nav li{position:absolute;top:19px;font-family:'Montserrat',sans-serif;font-size:13px;font-weight:600;color:var(--navy)}
.hero-copy{position:absolute;left:0;width:1200px;top:150px;text-align:center;z-index:2;color:var(--white)}
.hero-copy .eyebrow{font-family:'Montserrat',sans-serif;font-weight:700;font-size:21px;letter-spacing:.3px}
.hero-copy h1{color:var(--white);font-size:60px;font-weight:700;line-height:1.1;margin-top:6px}
.hero-copy p{width:560px;margin:18px auto 0;font-size:14px;line-height:1.65}
.hero-copy .btn-outline{display:inline-block;margin-top:40px;border:1px solid var(--white);background:rgba(15,25,40,.55);padding:9px 24px;font-family:'Montserrat',sans-serif;font-weight:600;font-size:13px}
.hero-arrow{position:absolute;top:225px;width:24px;height:50px;background:rgba(20,40,80,.8);z-index:2;display:flex;align-items:center;justify-content:center}

/* section titles */
.sec-title{font-size:28px;font-weight:700;color:var(--teal-dark);text-align:center}
.sec-intro{width:690px;margin:16px auto 0;text-align:center;font-size:13px}

/* services */
.services{top:635px;height:545px}
.services .sec-title{margin-top:100px}
.service-item{position:absolute;width:340px;display:flex;gap:18px}
.service-item svg{flex:none;margin-top:4px}
.service-item h3{font-size:17px;font-weight:600;color:var(--teal-dark);margin-bottom:6px}
.service-item p{font-size:13px;line-height:1.6}

/* plan */
.plan{top:1180px;height:557px;background:var(--grey-bg)}
.plan .chart{left:14px;top:155px}
.plan .copy{left:613px;top:118px;width:560px}
.eyebrow-small{font-family:'Montserrat',sans-serif;font-weight:600;font-size:17px;color:var(--teal-dark)}
.plan h2{font-size:28px;font-weight:700;margin-bottom:22px}
.plan p{font-size:13px;margin-bottom:16px}
.btn-line{display:inline-block;border:1px solid var(--navy);padding:7px 24px;font-family:'Montserrat',sans-serif;font-weight:600;font-size:12px;color:var(--navy)}

/* about */
.about{top:1737px;height:706px;background:var(--white)}
.about .intro{left:51px;top:118px;width:500px}
.about h2{font-size:26px;font-weight:700;margin-bottom:26px;white-space:nowrap}
.about .intro p{font-size:13px;margin-bottom:22px}
.brand-word{color:var(--teal)}
.feature-grid{left:613px;top:200px;width:560px;display:grid;grid-template-columns:280px 280px;row-gap:28px}
.feature-grid h3{font-size:16px;font-weight:600;color:var(--teal-dark);margin-bottom:6px}
.feature-grid p{font-size:13px;line-height:1.6}
.people{position:absolute;left:0;top:422px;width:1200px;height:284px;background:linear-gradient(180deg,#ffffff 0%,#eef0f3 55%,#dde1e6 100%)}

/* banner */
.banner{top:2443px;height:245px;background:linear-gradient(135deg,var(--teal) 0%,#0f6d6a 55%,#145b70 100%);text-align:center;color:#e4f1ee}
.banner h2{color:var(--white);font-size:28px;font-weight:600;margin-top:52px}
.banner p{width:620px;margin:14px auto 0;font-size:14px}
.banner .btn-solid{display:inline-block;margin-top:20px;background:var(--white);color:var(--navy);padding:6px 18px;font-family:'Montserrat',sans-serif;font-weight:600;font-size:12px}

/* why */
.why{top:2688px;height:412px;background:var(--grey-bg)}
.why .photo{left:0;top:0;width:559px;height:342px;background:linear-gradient(120deg,#cfd4d8,#9aa3ab 55%,#e4e7ea)}
.why .copy{left:582px;top:28px;width:600px}
.why h2{font-size:28px;font-weight:700;margin-bottom:16px}
.why .copy>p{font-size:13px;line-height:1.6}
.why-grid{display:grid;grid-template-columns:340px 260px;row-gap:18px;margin-top:22px}
.why-item{display:flex;gap:16px}
.why-item svg{flex:none;margin-top:2px}
.why-item h3{font-size:16px;font-weight:600;color:var(--teal-dark);margin-bottom:4px}
.why-item p{font-size:12px;line-height:1.55;width:210px}

/* contact */
.contact{top:3100px;height:656px}
.contact h2{font-size:27px;font-weight:600}
.callback{left:51px;top:108px;width:535px}
.callback>p,.faq>p{font-size:13px;margin-top:18px}
.field{position:absolute;height:34px;border:1px solid #d6d9de;font-size:12px;padding:7px 10px;color:#8b9098}
.submit{position:absolute;left:0;background:var(--navy);color:var(--white);font-family:'Montserrat',sans-serif;font-weight:600;font-size:12px;padding:7px 18px}
.faq{left:669px;top:108px;width:500px}
.faq ul{list-style:none;margin-top:32px}
.faq li{font-size:13px;color:var(--heading);display:flex;gap:18px;align-items:center;margin-bottom:26px}
.faq li b{width:18px;text-align:center;font-size:18px;font-weight:400;color:var(--heading)}
.faq .open b{background:var(--navy);color:var(--white);font-size:14px;line-height:18px}
.faq .open span{color:var(--navy)}
.faq .answer{display:block;margin:-14px 0 26px 36px;font-size:13px;color:var(--text);line-height:1.6}

/* footer */
.site-footer{top:3756px;height:479px;background:linear-gradient(135deg,var(--navy) 0%,#1b3f74 60%,#183660 100%);color:#c9d3e3}
.site-footer h4{color:var(--white);font-size:14px;font-weight:700;margin-bottom:22px}
.foot-col{position:absolute;top:108px;font-size:12px}
.foot-logo{font-family:'Montserrat',sans-serif;font-weight:800;font-size:27px;color:var(--white);margin-bottom:16px}
.newsletter{margin-top:26px;width:255px;height:36px;border:1px solid #6a7fa3;display:flex;justify-content:space-between;align-items:center;padding:0 12px;color:var(--white)}
.post h5{font-family:'Montserrat',sans-serif;color:var(--white);font-size:13px;font-weight:500;margin-bottom:4px}
.post{margin-bottom:20px;line-height:1.55}
.foot-col ul{list-style:none;line-height:2.45}
.foot-contact div{display:flex;gap:14px;margin-bottom:14px;line-height:1.55}
.copyright{position:absolute;left:0;bottom:0;width:1200px;height:80px;background:var(--navy-dark);text-align:center;line-height:80px;font-size:12px;color:#c9d3e3}
</style>
</head>
<body>

<div class="topbar">
  <div class="abs welcome">Welcome to Kryjto.cz</div>
  <div class="abs social"><span></span><span></span><span></span><span></span></div>
  <div class="abs search"></div>
</div>

<header class="site-header">
  <div class="abs logo">KRYJTO.CZ</div>
  <div class="abs header-band"></div>
  <div class="abs header-stripe"></div>
  <div class="abs contact-chip" style="left:468px">
    <svg width="26" height="26" viewBox="0 0 24 24" fill="none" stroke="#fff" stroke-width="1.5"><path d="M5 3h4l2 5-2.5 1.5a11 11 0 0 0 6 6L16 13l5 2v4a2 2 0 0 1-2 2A17 17 0 0 1 3 5a2 2 0 0 1 2-2z"/></svg>
    <div><strong>(+42) 555-018-2040</strong>We are open 9 am - 10pm</div>
  </div>
  <div class="abs contact-chip" style="left:736px">
    <svg width="28" height="22" viewBox="0 0 28 22" fill="none" stroke="#fff" stroke-width="1.5"><rect x="1" y="1" width="26" height="20"/><path d="M1 1l13 11L27 1"/></svg>
    <div><strong>hello@kryjto.cz</strong>You can mail us</div>
  </div>
  <div class="abs quote-btn">GET A QUOTE</div>
</header>

<nav class="main-nav">
  <ul>
    <li style="left:212px">HOME</li>
    <li style="left:334px">ABOUT US</li>
    <li style="left:428px">CASES</li>
    <li style="left:537px">SERVICES</li>
    <li style="left:656px">PROJECTS</li>
    <li style="left:758px">BLOG</li>
    <li style="left:843px">SHOP</li>
    <li style="left:940px">CONTACT</li>
  </ul>
</nav>

<section class="hero">
  <div class="hero-photo" role="img" aria-label="Photo of business people shaking hands in an office"></div>
  <div class="hero-arrow" style="left:0"><svg width="10" height="14" viewBox="0 0 10 14"><path d="M8 1L2 7l6 6" stroke="#fff" stroke-width="2" fill="none"/></svg></div>
  <div class="hero-arrow" style="right:0"><svg width="10" height="14" viewBox="0 0 10 14"><path d="M2 1l6 6-6 6" stroke="#fff" stroke-width="2" fill="none"/></svg></div>
  <div class="hero-copy">
    <div class="eyebrow">WE PROVIDE BEST FINANCIAL SOLUTIONS</div>
    <h1>FOR YOUR FINANCIAL PLAN</h1>
    <p>We have over 25 year's of experience in Finance and Business management so we can make your business more successful you can trust us</p>
    <span class="btn-outline">VIEW SERVICES</span>
  </div>
</section>

<section class="services">
  <h2 class="sec-title">Our Services</h2>
  <p class="sec-intro">Finvera amet sit amet, consectetur adipiscing elit, sed do eiusmod tempor incididunt ut labore et dolore magna aliqua. Ut enim ad minim veniam, quis nostrud exercitation ullamco</p>

  <div class="service-item" style="left:51px;top:237px">
    <svg width="34" height="34" viewBox="0 0 34 34" fill="none" stroke="#7a808a" stroke-width="1.5"><rect x="5" y="4" width="22" height="26"/><path d="M10 22l5-6 4 3 5-7"/></svg>
    <div><h3>Financial Planning</h3><p>Finvera consectetur adipiscing elit, sed do eiusmod tempor incididnt</p></div>
  </div>
  <div class="service-item" style="left:424px;top:237px">
    <svg width="34" height="34" viewBox="0 0 34 34" fill="none" stroke="#7a808a" stroke-width="1.5"><ellipse cx="14" cy="12" rx="9" ry="4"/><path d="M5 12v8c0 2 4 4 9 4s9-2 9-4v-8"/><circle cx="25" cy="22" r="6"/></svg>
    <div><h3>Cash Investment</h3><p>Finvera consectetur adipiscing elit, sed do eiusmod tempor incididnt</p></div>
  </div>
  <div class="service-item" style="left:805px;top:237px">
    <svg width="34" height="34" viewBox="0 0 34 34" fill="none" stroke="#7a808a" stroke-width="1.5"><rect x="4" y="10" width="26" height="18"/><path d="M12 10V6h10v4M4 17h26"/></svg>
    <div><h3>Financial Consultancy</h3><p>Finvera consectetur adipiscing elit, sed do eiusmod tempor incididnt</p></div>
  </div>
  <div class="service-item" style="left:51px;top:358px">
    <svg width="34" height="34" viewBox="0 0 34 34" fill="none" stroke="#7a808a" stroke-width="1.5"><path d="M3 16l7-6 7 4 7-4 7 6-10 9-4-3-4 3z"/></svg>
    <div><h3>Personal Insurance</h3><p>Finvera consectetur adipiscing elit, sed do eiusmod tempor incididnt</p></div>
  </div>
  <div class="service-item" style="left:424px;top:358px">
    <svg width="34" height="34" viewBox="0 0 34 34" fill="none" stroke="#7a808a" stroke-width="1.5"><circle cx="17" cy="17" r="12"/><path d="M17 10v14M13 13h6a2 2 0 0 1 0 4h-4a2 2 0 0 0 0 4h6"/></svg>
    <div><h3>Commodities Planning</h3><p>Finvera consectetur adipiscing elit, sed do eiusmod tempor incididnt</p></div>
  </div>
  <div class="service-item" style="left:805px;top:358px">
    <svg width="34" height="34" viewBox="0 0 34 34" fill="none" stroke="#7a808a" stroke-width="1.5"><path d="M5 29h24M8 29V17M15 29V12M22 29V15M28 29V8"/></svg>
    <div><h3>Retirement Planning</h3><p>Finvera consectetur adipiscing elit, sed do eiusmod tempor incididnt</p></div>
  </div>
</section>

<section class="plan">
  <svg class="abs chart" width="540" height="300" viewBox="0 0 540 300" aria-label="Area chart of plan growth">
    <g font-family="Poppins,sans-serif" font-size="10" fill="#6b7078">
      <text x="6" y="16">80</text><text x="6" y="86">60</text><text x="6" y="156">40</text><text x="6" y="226">20</text><text x="10" y="274">0</text>
      <text x="135" y="288">2</text><text x="220" y="288">4</text><text x="305" y="288">6</text><text x="390" y="288">8</text><text x="470" y="288">10</text>
      <text x="4" y="296" font-size="8">The Version</text>
    </g>
    <line x1="50" y1="270" x2="520" y2="270" stroke="#c4c8ce"/>
    <line x1="50" y1="10" x2="50" y2="270" stroke="#c4c8ce"/>
    <path d="M50 270C95 270 110 96 140 96S190 270 225 270Z" fill="#1f8f78"/>
    <path d="M140 270C185 270 195 10 225 10S270 270 310 270Z" fill="#1f3f72"/>
    <path d="M225 270C265 270 280 120 310 120S350 270 390 270Z" fill="#1f8f78"/>
    <path d="M310 270C350 270 360 48 390 48S430 270 470 270Z" fill="#1f3f72"/>
    <path d="M390 270C420 270 445 122 470 122S505 270 520 270Z" fill="#1f8f78"/>
    <g fill="#fff" stroke="#9fb4cf"><circle cx="140" cy="240" r="3"/><circle cx="225" cy="190" r="3"/><circle cx="310" cy="240" r="3"/><circle cx="390" cy="200" r="3"/><circle cx="470" cy="245" r="3"/></g>
  </svg>
  <div class="abs copy">
    <div class="eyebrow-small">We Provide Best</div>
    <h2>Financial Plan for You</h2>
    <p>Finvera amet, ut perspiciatis unde omnis iste natus error sit voluptatem accusantium ipsum dolor sit amet, situr adipiscing elit, sed do eiusmod tempor incididunt ut labore et dolore magna aliqua. Ut enim ad minim veniam, quis nostrud exercitation ullamco laboris nisi ut aliquip ex ea commodo consequatur.</p>
    <p>Finvera amet, ut perspiciatis unde omnis iste natus error sit voluptatem accusantium que laudantium, totam rem aperiam, eaque ipsa quae ab illo inventore veritatis ipsum dolor sit amet, consectetur</p>
    <span class="btn-line">LEARN MORE</span>
  </div>
</section>

<section class="about">
  <div class="people" role="img" aria-label="Photo of business people in suits standing and discussing"></div>
  <div class="abs intro">
    <div class="eyebrow-small" style="color:var(--heading)">We are <span class="brand-word">KRYJTO.CZ</span></div>
    <h2>Your Complete Financial Solutions</h2>
    <p>Finvera amet, consectetur adipiscing elit, sed do eiusmod tempor ut labore et dolore magna aliqua. Ut enim ad minim iam, quis norud exta exercitation ullamco laboris nisi ut aliquip exea comme consequat. Duis aute irure dolor in reprehenderit</p>
    <p>Finvera amet, consectetur adipiscing elit, sed do eiusmod tempor incidi utinfis on the labore et dolore magna aliqua enim ad minimiam.</p>
  </div>
  <div class="abs feature-grid">
    <div><h3>Financial Service</h3><p>Finvera consectetur adipiscing elit,<br>sed do eiusmod tempor incididnt</p></div>
    <div><h3>Best Consultancy</h3><p>Finvera consectetur adipiscing elit,<br>sed do eiusmod tempor incididnt</p></div>
    <div><h3>Business Analysis</h3><p>Finvera consectetur adipiscing elit,<br>sed do eiusmod tempor incididnt</p></div>
    <div><h3>24/7 Support</h3><p>Finvera consectetur adipiscing elit,<br>sed do eiusmod tempor incididnt</p></div>
  </div>
</section>

<section class="banner">
  <h2>We Provide Best Financial Services for your Business</h2>
  <p>We have over 25 year's of experience in Finance and Business management so we can make your business more successful you can trust us and we care about it</p>
  <span class="btn-solid">BUY NOW</span>
</section>

<section class="why">
  <div class="abs photo" role="img" aria-label="Photo of a businesswoman with colleagues working at a laptop in an office"></div>
  <div class="abs copy">
    <div class="eyebrow-small">Why You</div>
    <h2>Choose Finvera</h2>
    <p>Finvera amet, ut perspiciatis unde omnis iste natus error sit voluptatem accusantium ipsum dolor sit amet, situr adipiscing elit, sed do eiusmod tempor incididunt ut labore et dolore magna.</p>
    <div class="why-grid">
      <div class="why-item">
        <svg width="26" height="26" viewBox="0 0 26 26" fill="none" stroke="#7a808a" stroke-width="1.5"><path d="M4 22l5-2 12-12a3 3 0 0 0-4-4L5 16z"/></svg>
        <div><h3>Fast Loan Approval</h3><p>Finvera consectetur adipiscing elit, sed do eiusmod tempor incididnt</p></div>
      </div>
      <div class="why-item">
        <svg width="26" height="26" viewBox="0 0 26 26" fill="none" stroke="#7a808a" stroke-width="1.5"><circle cx="9" cy="9" r="4"/><circle cx="18" cy="10" r="3"/><path d="M2 22c0-5 3-8 7-8s7 3 7 8M16 16c4 0 7 2 7 6"/></svg>
        <div><h3>Dedicated Team</h3><p>Finvera consectetur adipiscing elit, sed do eiusmod tempor incididnt</p></div>
      </div>
      <div class="why-item">
        <svg width="26" height="26" viewBox="0 0 26 26" fill="none" stroke="#7a808a" stroke-width="1.5"><rect x="5" y="3" width="16" height="20"/><path d="M9 9h8M9 13h8M9 17h5"/></svg>
        <div><h3>Free Documentation</h3><p>Finvera consectetur adipiscing elit, sed do eiusmod tempor incididnt</p></div>
      </div>
      <div class="why-item">
        <svg width="26" height="26" viewBox="0 0 26 26" fill="none" stroke="#7a808a" stroke-width="1.5"><path d="M21 13a8 8 0 1 1-3-6.2M21 4v5h-5"/></svg>
        <div><h3>Refinancing</h3><p>Finvera consectetur adipiscing elit, sed do eiusmod tempor incididnt</p></div>
      </div>
    </div>
  </div>
</section>

<section class="contact">
  <div class="abs callback">
    <h2>Reqeust a Call Back</h2>
    <p>Finvera amet sit amet, consectetur adipiscing elit, sed do eiusmod tempor incididunt ut labore et dolore magna aliqua enim ad minim veniam</p>
    <div style="position:relative">
      <div class="field" style="left:0;top:32px;width:287px">Name</div>
      <div class="field" style="left:286px;top:32px;width:287px">Email</div>
      <div class="field" style="left:0;top:86px;width:287px">Subject</div>
      <div class="field" style="left:286px;top:86px;width:287px">Phone</div>
      <div class="field" style="left:0;top:138px;width:573px;height:142px">Message</div>
    </div>
    <span class="submit" style="top:410px">SUBMIT NOW</span>
  </div>
  <div class="abs faq">
    <h2>Frequently Ask Qustion</h2>
    <p>Finvera amet sit amet, consectetur adipiscing elit, sed do eiusmod temp incididunt ut labore et dolore magna aliqua enim ad minim veniam</p>
    <ul>
      <li class="open"><b>−</b><span>What kind of Financial Consultancy you need</span></li>
      <li class="answer">Sed ut perspiciatis unde omnis iste natus error sit volu totam accusantium doloremque laudantium totam rem, eaque ipsa quae ab illo invet</li>
      <li><b>+</b><span>How we help you for your Business</span></li>
      <li><b>+</b><span>Financial Advice</span></li>
      <li><b>+</b><span>What is the best Business plan for you</span></li>
      <li><b>+</b><span>Which is the right plan for Retirement</span></li>
    </ul>
  </div>
</section>

<footer class="site-footer">
  <div class="foot-col" style="left:51px;width:270px">
    <div class="foot-logo">KRYJTO.CZ</div>
    <p>Lorem must explain to you how all this mistaken idea of pleasure and praising pain was born and I will give you a complete plan we prepare to you lorem</p>
    <div class="newsletter"><span style="color:#c9d3e3">Email for Newsletter</span>
      <svg width="14" height="14" viewBox="0 0 14 14"><path d="M1 7L13 1 9 13 7 8z" fill="#fff"/></svg></div>
  </div>
  <div class="foot-col" style="left:395px;width:230px">
    <h4>POPULAR POST</h4>
    <div class="post"><h5>Duplex Villa Design</h5>Lorem ipsum dolor sit amet, tur<br>acngit sed do eius</div>
    <div class="post"><h5>Real Estate Firm</h5>Lorem ipsum dolor sit amet, tur<br>acngit sed do eius</div>
  </div>
  <div class="foot-col" style="left:680px">
    <h4>QUICK LINK</h4>
    <ul><li>About us</li><li>Services</li><li>Projects</li><li>CASES</li><li>From Blog</li><li>Contact</li></ul>
  </div>
  <div class="foot-col foot-contact" style="left:918px;width:250px">
    <h4>CONTACT US</h4>
    <div><svg width="14" height="16" viewBox="0 0 14 16" fill="none" stroke="#c9d3e3"><path d="M7 15s5-5 5-9A5 5 0 0 0 2 6c0 4 5 9 5 9z"/><circle cx="7" cy="6" r="2"/></svg><span>Vlněna 14<br>Brno, Czechia</span></div>
    <div><svg width="14" height="14" viewBox="0 0 24 24" fill="none" stroke="#c9d3e3" stroke-width="2"><path d="M5 3h4l2 5-2.5 1.5a11 11 0 0 0 6 6L16 13l5 2v4a2 2 0 0 1-2 2A17 17 0 0 1 3 5a2 2 0 0 1 2-2z"/></svg><span>Telephone : (+42) 555-018-2040<br>Telephone : (+42) 555-018-2041</span></div>
    <div><svg width="14" height="12" viewBox="0 0 28 22" fill="none" stroke="#c9d3e3" stroke-width="2"><rect x="1" y="1" width="26" height="20"/><path d="M1 1l13 11L27 1"/></svg><span>Email : hello@kryjto.cz<br>Web : www.kryjto.cz</span></div>
  </div>
  <div class="copyright">Copyright© 2017 Kryjto.cz . All rights reserved.</div>
</footer>

</body>
</html>
```